South Carolina Bridal and Formal Wear Store

We want The Gown Parlor of Ashcombe website to feel luxurious, elegant, welcoming, and approachable—without feeling overpriced or intimidating. The site should immediately show that we are a full-service bridal and formal wear destination, offering bridal gowns, prom, mothers’ dresses, tuxedos and suits, accessories, and more. We want beautiful, high-end imagery and a clean, modern design while still reflecting the warm, personal experience customers receive when they walk into our boutique. Most importantly, the website should be easy to shop and navigate, allowing customers to browse our collections, see what we offer, understand price ranges, book appointments, and feel excited and comfortable choosing The Gown Parlor of Ashcombe for all of their special-event needs.

Target Market(s)

Women ages 18-50. Brides, engaged women, mothers of the occasion

Industry/Entity Type

Bridal and Formal Wear

Coding

Coded - Design and coding required

Number of Pages Required

5+ page

Font styles to use
Sans Serif

Colors

Designer to choose colors to be used in the design.

Requirements
Must have
• Appointment area, about us staff area, what we offer and designers our logo
Nice to have
• Modern Southern Luxury: Clean, elegant, and upscale with soft neutral tones, beautiful bridal photography, and a warm Lowcountry feel.
Should not have
• pricing

```html
<!DOCTYPE html>
<html lang="en">
<head>
<meta charset="utf-8">
<title>The Gown Parlor of Ashcombe — Formal Wear</title>
<link href="https://fonts.googleapis.com/css2?family=Inter:wght@400;500;600;700&display=swap" rel="stylesheet">
<style>
:root{
  --ink:#111111;
  --bar:#0b0b0b;
  --cream:#f9f7f3;
  --sand:#f4f0ea;
  --stone:#efe9df;
  --muted:#4a4643;
  --taupe:#9c8466;
  --gold:#d6b27a;
  --white:#ffffff;
}
*{box-sizing:border-box;margin:0;padding:0}
html,body{width:918px;height:1200px;overflow:hidden}
body{font-family:"Inter",Helvetica,Arial,sans-serif;color:var(--ink);background:var(--sand);position:relative}
.abs{position:absolute}

.topbar{left:0;top:0;width:918px;height:14px;background:var(--bar);color:#bdb7ae;font-size:5.2px;letter-spacing:.9px;text-transform:uppercase;display:flex;align-items:center;justify-content:center;gap:5px}
.topbar .accent{color:var(--gold)}
.nav{left:0;top:14px;width:918px;height:42px;background:var(--bar);border-top:1px solid #1c1c1c}
.brand{left:110px;top:13px;color:#f0ebe3;font-size:8.5px;font-weight:500;letter-spacing:.3px;line-height:1.2;width:100px}
.menu{left:332px;top:18px;display:flex;gap:17px;font-size:5.8px;font-weight:600;letter-spacing:1.1px;color:#e9e4dc;text-transform:uppercase}
.menu .active{color:var(--white);border-bottom:1px solid var(--white);padding-bottom:4px}
.cta-top{left:700px;top:10px;width:118px;height:22px;background:var(--stone);color:var(--ink);font-size:5.8px;font-weight:700;letter-spacing:1px;display:flex;align-items:center;justify-content:center;gap:6px}

.hero{left:8px;top:56px;width:910px;height:346px;background:linear-gradient(100deg,#5a6a7c 0%,#8a8a8f 28%,#cfc6bd 48%,#9aa7bd 70%,#6c80a3 100%)}
.hero-shade{left:8px;top:56px;width:910px;height:346px;background:linear-gradient(90deg,rgba(20,20,25,.55) 0%,rgba(20,20,25,.25) 55%,rgba(20,20,25,.05) 100%)}
.hero-eyebrow{left:143px;top:122px;font-size:5.6px;font-weight:700;letter-spacing:1.4px;color:#e8d7bf}
.hero-title{left:141px;top:128px;width:420px;font-size:50px;line-height:49px;font-weight:500;letter-spacing:-2.6px;color:var(--white)}
.hero-sub{left:143px;top:338px;width:300px;font-size:9.8px;line-height:17px;color:#efebe6}
.hero-tags{left:748px;top:375px;font-size:5.4px;letter-spacing:.9px;color:#e6e1da}

.formal{left:5px;top:402px;width:913px;height:396px;background:var(--cream)}
.eyebrow{font-size:5.6px;font-weight:700;letter-spacing:1.4px;color:var(--taupe);display:flex;align-items:center;gap:6px}
.eyebrow::before{content:"";width:20px;height:1px;background:var(--taupe)}
.formal-eyebrow{left:139px;top:482px}
.section-title{font-size:34px;line-height:36.5px;font-weight:500;letter-spacing:-1.6px;color:var(--ink)}
.formal-title{left:139px;top:497px;width:300px}
.formal-lead{left:139px;top:617px;width:310px;font-size:9.6px;line-height:17px;color:var(--muted)}
.formal-note{left:139px;top:661px;width:310px;font-size:7.4px;line-height:13.7px;color:var(--muted)}
.btn{left:139px;top:695px;width:148px;height:26px;background:var(--ink);color:var(--white);font-size:5.9px;font-weight:700;letter-spacing:1px;display:flex;align-items:center;justify-content:center;gap:7px}
.arch{left:549px;top:443px;width:236px;height:281px;border-radius:56px 56px 3px 3px;background:linear-gradient(160deg,#6d7268 0%,#d9d3cb 35%,#f1d4c8 60%,#e9c5b4 80%,#b87a5c 100%)}
.inset{left:517px;top:631px;width:102px;height:125px;background:var(--white);padding:3px;box-shadow:0 4px 14px rgba(0,0,0,.08)}
.inset div{width:100%;height:100%;background:linear-gradient(170deg,#7f8d63 0%,#d8cfc0 45%,#e8c8bb 75%,#a58a6f 100%)}

.palette-title{left:133px;top:795px;width:260px}
.palette-copy{left:462px;top:866px;width:305px;font-size:9.5px;line-height:17px;color:var(--muted)}
.photo{top:929px;height:271px;border-radius:4px 4px 0 0}
.photo-a{left:133px;width:231px;background:linear-gradient(180deg,#9aa27c 0%,#6f7d56 40%,#8db3c4 75%,#7a8a5a 100%)}
.photo-b{left:373px;top:956px;width:168px;height:244px;background:linear-gradient(180deg,#6f7a57 0%,#a6a99a 40%,#8d9099 70%,#b9cbe0 100%)}
.photo-c{left:550px;width:232px;background:linear-gradient(180deg,#5f8a4c 0%,#c9a68c 40%,#eae2d8 65%,#7fa9c9 100%)}
.to-top{left:885px;top:1169px;width:21px;height:21px;border-radius:50%;background:var(--white);border:1px solid #ddd6cc;display:flex;align-items:center;justify-content:center}
</style>
</head>
<body>
<div class="abs topbar"><span>Ashcombe, South Carolina</span><span>·</span><span>Wednesday–Saturday 10am–6pm</span><span>·</span><span class="accent">Appointments recommended</span></div>
<header class="abs nav"></header>
<div class="abs brand">The Gown Parlor of Ashcombe</div>
<nav class="abs menu"><span>Collections</span><span class="active">Formal Wear</span><span>Tuxedos</span><span>Designers</span><span>The House</span></nav>
<div class="abs cta-top">REQUEST APPOINTMENT <svg width="7" height="5" viewBox="0 0 7 5"><path d="M0 2.5h6M4 .5l2 2-2 2" stroke="#111" fill="none" stroke-width=".8"/></svg></div>

<div class="abs hero" role="img" aria-label="Close view of a bride in lace with bridesmaids in blue floral dresses"></div>
<div class="abs hero-shade"></div>
<div class="abs hero-eyebrow">FORMAL WEAR, BEAUTIFULLY CONSIDERED</div>
<h1 class="abs hero-title">Every special occasion deserves its own kind of entrance.</h1>
<p class="abs hero-sub">Prom, bridesmaids and mothers of the occasion—curated to feel polished, personal and easy to shop.</p>
<div class="abs hero-tags">FORMAL WEAR · PROM · MOTHERS · BRIDESMAIDS</div>

<section class="abs formal"></section>
<div class="abs eyebrow formal-eyebrow">PROM &amp; FORMAL</div>
<h2 class="abs section-title formal-title">The dress that changes the whole night.</h2>
<p class="abs formal-lead">From sleek and understated to full-volume glamour, discover formal gowns made for the moment the room turns your way.</p>
<p class="abs formal-note">A dedicated formalwear appointment gives you space to try different shapes, colors and moods without rushing the experience.</p>
<div class="abs btn">BOOK A FORMAL APPOINTMENT <svg width="7" height="5" viewBox="0 0 7 5"><path d="M0 2.5h6M4 .5l2 2-2 2" stroke="#fff" fill="none" stroke-width=".8"/></svg></div>
<div class="abs arch" role="img" aria-label="Woman in a blush ruffled ball gown on brick steps among roses"></div>
<div class="abs inset" role="img" aria-label="Couple embracing in a blush gown in a garden courtyard"><div></div></div>

<h2 class="abs section-title palette-title">A palette that looks effortless together.</h2>
<p class="abs palette-copy">Coordinate your wedding party with designer options from Marivelle, Dessa Row Collection, Alden Sorrel, Half Past Six and Gentle Maids.</p>
<div class="abs photo photo-a" role="img" aria-label="Bride with bridesmaids in dusty blue gowns walking through pines"></div>
<div class="abs photo photo-b" role="img" aria-label="Wedding party in grey suits and pale blue dresses under live oaks"></div>
<div class="abs photo photo-c" role="img" aria-label="Bride with bridesmaids in blue floral dresses among palms"></div>
<div class="abs to-top"><svg width="9" height="11" viewBox="0 0 9 11"><path d="M4.5 10.5V1M1 4.5l3.5-3.5L8 4.5" stroke="#111" fill="none" stroke-width="1.2"/></svg></div>
</body>
</html>
```